Website Design for Wheels for Heroes.org - Donated Cars to Disabled Vets

Need a Wordpress website. The coding now, esp. the CDONT coding is not supported by many hosting sites. Looking for a landing page to generate leads.

Logo Text

look at current one for ideas

Coding

Coded - Design and coding required

Number of Pages Required

1 page

Requirements
Must have
• look at current website at www.wheelsforheroes.org
Nice to have
• look at this site: http://givemotortoservicemen.org

```html
<!DOCTYPE html>
<html lang="en">
<head>
<meta charset="utf-8">
<title>Wheels for Heroes – Donate Your Car</title>
<link href="https://fonts.googleapis.com/css2?family=Open+Sans:wght@400;600;700&family=Raleway:wght@500;600;700&display=swap" rel="stylesheet">
<style>
:root{
  --blue:#1a56b0;
  --blue-dark:#134a9c;
  --blue-light:#2a74d6;
  --red:#b71c1c;
  --red-bright:#c62828;
  --grey-bg:#f2f3f5;
  --text:#555;
  --muted:#9a9a9a;
  --dark:#3f3f3f;
  --white:#fff;
}
*{box-sizing:border-box;margin:0;padding:0}
html,body{width:1200px;height:2198px;overflow:hidden}
body{font-family:"Open Sans",Arial,sans-serif;color:var(--text);background:var(--white);position:relative}
.abs{position:absolute}

/* header */
.topbar{left:0;top:0;width:1200px;height:88px;background:linear-gradient(180deg,var(--blue-light),var(--blue))}
.brand{left:92px;top:22px;display:flex;align-items:center;gap:12px;color:var(--white);font-family:"Raleway",sans-serif;font-weight:600;font-size:26px}
.brand-mark{width:28px;height:28px;background:var(--red);border-radius:4px}
.tollfree{left:872px;top:16px;display:flex;align-items:center;gap:16px;color:var(--white)}
.tollfree-icon{width:46px;height:46px;border:2px solid var(--white);border-radius:50%;display:flex;align-items:center;justify-content:center}
.tollfree small{display:block;font-size:15px}
.tollfree strong{display:block;font-size:25px;font-weight:600;letter-spacing:.3px}
.nav{left:0;top:88px;width:1200px;height:53px;background:var(--blue-dark)}
.nav ul{list-style:none;display:flex;position:absolute;left:124px;top:19px}
.nav li{color:var(--white);font-size:12.5px;font-weight:600;text-transform:uppercase;margin-right:57px}

/* hero */
.hero{left:0;top:141px;width:1200px;height:471px;background:linear-gradient(180deg,#6c7c8e 0%,#b88d67 45%,#4a3a30 70%,#2b2522 100%)}
.dots{left:87px;top:584px;display:flex;gap:6px}
.dots span{width:12px;height:12px;border:2px solid var(--white);border-radius:50%}
.dots .on{background:var(--red)}
.donate-panel{left:803px;top:88px;width:310px;height:417px;background:rgba(60,60,60,.88)}
.donate-head{height:53px;background:var(--red-bright);color:var(--white);font-family:"Raleway",sans-serif;font-weight:700;font-size:20px;padding:14px 19px}
.donate-panel p{color:var(--white);font-size:11.5px;padding:16px 0 0 20px}
.field{position:absolute;background:var(--white);height:35px;font-size:11px;color:#666;padding:10px 12px;border-radius:2px}
.btn-donate{position:absolute;left:74px;top:377px;width:162px;height:40px;background:var(--red-bright);color:var(--white);font-size:14px;font-weight:600;text-align:center;line-height:40px;border-radius:2px;box-shadow:0 2px 3px rgba(0,0,0,.3)}

/* program */
.program-title{left:0;top:650px;width:1200px;text-align:center;font-family:"Raleway",sans-serif;font-size:22px;font-weight:600;color:#555}
.program-intro{left:270px;top:690px;width:660px;text-align:center;font-size:11.5px;line-height:23px;color:var(--muted)}
.feature{top:776px;width:240px;text-align:center}
.feature-icon{width:114px;height:114px;margin:0 auto;border-radius:50%;border:2px solid;display:flex;align-items:center;justify-content:center}
.feature-icon .disc{width:104px;height:104px;border-radius:50%;display:flex;align-items:center;justify-content:center}
.feature.blue .feature-icon{border-color:var(--blue)}.feature.blue .disc{background:var(--blue)}
.feature.red .feature-icon{border-color:var(--red)}.feature.red .disc{background:var(--red)}
.feature h3{font-size:15px;font-weight:600;margin-top:14px}
.feature.blue h3,.feature.blue a{color:var(--blue)}
.feature.red h3,.feature.red a{color:var(--red)}
.feature p{font-size:11.5px;line-height:23px;color:var(--muted);margin-top:10px}
.feature a{display:inline-block;font-size:12px;font-weight:700;text-decoration:underline;margin-top:5px}

/* why */
.why{left:0;top:1072px;width:1200px;height:405px;background:var(--grey-bg)}
.why-photo{left:0;top:1072px;width:440px;height:405px;background:linear-gradient(120deg,#fafafa 0%,#d4d6d9 40%,#9ea3a8 70%,#ececec 100%)}
.why-title{left:501px;top:1103px;font-family:"Raleway",sans-serif;font-size:20px;font-weight:600;color:#555}
.why-intro{left:501px;top:1140px;width:620px;font-size:11.5px;line-height:22px;color:#777}
.why-item{left:501px;width:610px;display:flex;gap:30px;font-size:12.5px;line-height:24px;color:#666}
.why-num{flex:none;width:34px;height:34px;border-radius:50%;background:var(--blue);color:var(--white);font-size:11px;font-weight:700;display:flex;align-items:center;justify-content:center;box-shadow:0 0 0 3px #cfdaf0}
.why-item b{color:#444;font-weight:600}

/* split */
.split{left:0;top:1480px;width:1200px;height:372px}
.split-title{font-family:"Raleway",sans-serif;font-size:20px;font-weight:700;color:var(--white)}
.split-text{font-size:11.5px;line-height:23px;color:var(--white)}
.about-item{left:87px;display:flex;gap:20px;color:var(--white)}
.about-icon{flex:none;width:46px;height:46px;border:2px solid var(--white);border-radius:50%;display:flex;align-items:center;justify-content:center}
.about-item h4{font-size:15px;font-weight:600;margin-top:2px}
.about-item p{font-size:10px;line-height:20px;color:#c7d6f0;margin-top:2px}
.checks{left:668px;top:1640px;list-style:none}
.checks li{display:flex;align-items:center;gap:18px;color:var(--white);font-size:11.5px;height:36.6px}

/* footer */
.foot-col{top:1910px}
.foot-col h5{font-family:"Raleway",sans-serif;font-size:16px;font-weight:600;color:#555;letter-spacing:.4px}
.badge-box{width:146px;height:66px;background:#e6e6e6;border-radius:4px}
.badge-seal{width:66px;height:66px;background:#d7e3f2;border-radius:50%;border:3px solid #8fb0da}
.contact-list{list-style:none;margin-top:22px}
.contact-list li{display:flex;gap:14px;font-size:11.5px;color:#666;line-height:15px;margin-bottom:14px}
.contact-list a{color:#666}
.foot-col p{font-size:11.5px;line-height:20px;color:#888;margin-top:20px}
.email-box{width:212px;height:33px;border:1px solid #ddd;font-size:11.5px;color:#666;padding:8px 14px;margin-top:18px}
.btn-sub{display:inline-block;margin-top:15px;background:var(--blue);color:var(--white);font-size:10.5px;font-weight:600;padding:6px 10px}
.social{display:flex;gap:8px;margin-top:22px}
.social span{width:35px;height:35px;border:1px solid #bbb;border-radius:50%}
.copyright{left:0;top:2132px;width:1200px;height:66px;background:var(--dark);color:var(--white);font-size:12px;text-align:center;padding-top:24px}
</style>
</head>
<body>

<header>
  <div class="abs topbar"></div>
  <div class="abs brand"><span class="brand-mark"></span>Wheels for Heroes</div>
  <div class="abs tollfree">
    <div class="tollfree-icon"><svg width="20" height="20" viewBox="0 0 24 24"><path fill="#fff" d="M6.6 10.8a15 15 0 0 0 6.6 6.6l2.2-2.2c.3-.3.7-.4 1-.2 1.1.4 2.3.6 3.6.6.6 0 1 .4 1 1V20c0 .6-.4 1-1 1A17 17 0 0 1 3 4c0-.6.4-1 1-1h3.5c.6 0 1 .4 1 1 0 1.3.2 2.5.6 3.6.1.3 0 .7-.2 1z"/></svg></div>
    <div><small>Call toll-free</small><strong>1-800-555-0142</strong></div>
  </div>
  <nav class="abs nav">
    <ul><li>Home</li><li>About Us</li><li>Services</li><li>How It Works</li><li>Charities</li><li>Contact Us</li></ul>
  </nav>
</header>

<section>
  <div class="abs hero" role="img" aria-label="Photo of a dark luxury sedan on an open road at sunset"></div>
  <div class="abs dots"><span></span><span class="on"></span><span></span><span></span></div>
  <form class="abs donate-panel">
    <div class="donate-head">DONATE HERE</div>
    <p>Fill out the form below to instantly donate online</p>
    <div class="field" style="left:20px;top:106px;width:133px">Name :</div>
    <div class="field" style="left:158px;top:106px;width:133px">Phone :</div>
    <div class="field" style="left:20px;top:150px;width:271px">Email :</div>
    <div class="field" style="left:20px;top:194px;width:271px">Address :</div>
    <div class="field" style="left:20px;top:238px;width:271px">City :</div>
    <div class="field" style="left:20px;top:282px;width:271px">State :
      <svg style="position:absolute;right:12px;top:14px" width="10" height="6"><path d="M0 0h10L5 6z" fill="#666"/></svg></div>
    <div class="field" style="left:20px;top:326px;width:271px">Zip Code :</div>
    <div class="btn-donate">DONATE NOW!</div>
  </form>
</section>

<section>
  <h2 class="abs program-title">CAR DONATION PROGRAM</h2>
  <p class="abs program-intro">Sed ut perspiciatis unde omnis iste natus error sit voluptatem accusantium doloremque laudantium, totam rem aperiam ab illo inventore veritatis et quasi architecto beatae vitae dicta sunt explicabo.</p>

  <div class="abs feature blue" style="left:89px">
    <div class="feature-icon"><div class="disc"><svg width="54" height="50" viewBox="0 0 54 50"><path d="M27 26C20 20 15 16 15 11a6 6 0 0 1 12-1 6 6 0 0 1 12 1c0 5-5 9-12 15z" fill="#fff"/><path d="M4 22l10 16h14M50 22L40 38H26" stroke="#fff" stroke-width="4" fill="none" stroke-linejoin="round"/></svg></div></div>
    <h3>Donations Accepted</h3>
    <p>Sed ut perspiciatis unde omnis iste natus beatae vitae dicta sunt explicabo.</p>
    <a>READ MORE</a>
  </div>
  <div class="abs feature red" style="left:349px">
    <div class="feature-icon"><div class="disc"><svg width="62" height="34" viewBox="0 0 62 34"><path d="M4 16l8-12h26l12 12h8v10H4z" fill="#fff"/><circle cx="16" cy="27" r="6" fill="#b71c1c" stroke="#fff" stroke-width="3"/><circle cx="47" cy="27" r="6" fill="#b71c1c" stroke="#fff" stroke-width="3"/><path d="M15 7h10v8H10zM29 7h8l8 8H29z" fill="#b71c1c"/></svg></div></div>
    <h3>All Vehicle Type</h3>
    <p>Sed ut perspiciatis unde omnis iste natus beatae vitae dicta sunt explicabo.</p>
    <a>READ MORE</a>
  </div>
  <div class="abs feature blue" style="left:609px">
    <div class="feature-icon"><div class="disc"><svg width="40" height="50" viewBox="0 0 40 50"><rect x="2" y="2" width="36" height="46" rx="3" fill="none" stroke="#fff" stroke-width="4"/><path d="M10 14h20M10 22h20M10 30h12M10 38h12" stroke="#fff" stroke-width="3"/><circle cx="30" cy="36" r="5" fill="#fff"/></svg></div></div>
    <h3>Tax Deductible</h3>
    <p>Sed ut perspiciatis unde omnis iste natus beatae vitae dicta sunt explicabo.</p>
    <a>READ MORE</a>
  </div>
  <div class="abs feature red" style="left:869px">
    <div class="feature-icon"><div class="disc"><svg width="62" height="46" viewBox="0 0 62 46"><path d="M4 18h16V8h10l6 10h8V32H4z" fill="#fff"/><path d="M36 18L52 4v18" stroke="#fff" stroke-width="4" fill="none"/><circle cx="14" cy="35" r="6" fill="#b71c1c" stroke="#fff" stroke-width="3"/><circle cx="36" cy="35" r="6" fill="#b71c1c" stroke="#fff" stroke-width="3"/></svg></div></div>
    <h3>Towing Free</h3>
    <p>Sed ut perspiciatis unde omnis iste natus beatae vitae dicta sunt explicabo.</p>
    <a>READ MORE</a>
  </div>
</section>

<section>
  <div class="abs why"></div>
  <div class="abs why-photo" role="img" aria-label="Photo of a silver hatchback car, side view"></div>
  <h2 class="abs why-title">WHY DONATE YOUR CAR TO US?</h2>
  <p class="abs why-intro">Complete the form and a representative will call you to arrange a convenient time to pickup your car.And benefit Heroes Mobility Support Fund. An IRS 501(c)3 nonprofit organization.</p>
  <div class="abs why-item" style="top:1208px"><span class="why-num">01</span><div style="padding-top:5px"><b>IRS 501(C)3 APPROVED :</b> Free 24/7 Pickup with No DMV Hassles.</div></div>
  <div class="abs why-item" style="top:1262px"><span class="why-num">02</span><div><b>FREE LOCAL TOWING :</b> We will pick up your car donation, running or not, when it's most convenient, at home or work.</div></div>
  <div class="abs why-item" style="top:1328px"><span class="why-num">03</span><div style="padding-top:5px"><b>ALL CARS ACCEPTED :</b> We take your car regardless of its condition or registration status.</div></div>
  <div class="abs why-item" style="top:1384px"><span class="why-num">04</span><div><b>INCOME TAX DEDUCTION :</b> We issue you an IRS tax receipt &amp; offer the largest resale network to get you the highest tax write-off possible.</div></div>
</section>

<section>
  <svg class="abs split" viewBox="0 0 1200 372" width="1200" height="372">
    <rect width="1200" height="372" fill="var(--red)"/>
    <path d="M0 0H637L542 372H0z" fill="var(--blue)"/>
  </svg>
  <h2 class="abs split-title" style="left:87px;top:1507px">ABOUT US</h2>
  <p class="abs split-text" style="left:87px;top:1546px;width:490px">Sed ut perspiciatis unde omnis iste natus error sit voluptatem accusantium doloremque laudantium, totam rem aperiam, eaque ipsa quae ab illo sv</p>
  <div class="abs about-item" style="top:1609px">
    <div class="about-icon"><svg width="18" height="18" viewBox="0 0 24 24"><path fill="#fff" d="M6.6 10.8a15 15 0 0 0 6.6 6.6l2.2-2.2c.3-.3.7-.4 1-.2 1.1.4 2.3.6 3.6.6.6 0 1 .4 1 1V20c0 .6-.4 1-1 1A17 17 0 0 1 3 4c0-.6.4-1 1-1h3.5c.6 0 1 .4 1 1 0 1.3.2 2.5.6 3.6.1.3 0 .7-.2 1z"/></svg></div>
    <div><h4>CALL US</h4><p>Sed ut perspiciatis unde omnis iste natus error sit volup-<br>tatem accusantium doloremque</p></div>
  </div>
  <div class="abs about-item" style="top:1689px">
    <div class="about-icon"><svg width="22" height="16" viewBox="0 0 22 16"><path d="M1 2h12v9H1zM13 5h5l3 4v2h-8z" fill="#fff"/><circle cx="5" cy="13" r="2.5" fill="#fff"/><circle cx="17" cy="13" r="2.5" fill="#fff"/></svg></div>
    <div><h4>WE TOW IT</h4><p>Sed ut perspiciatis unde omnis iste natus error sit volup-<br>tatem accusantium doloremque</p></div>
  </div>
  <div class="abs about-item" style="top:1769px">
    <div class="about-icon"><svg width="16" height="20" viewBox="0 0 16 20"><rect x="1" y="1" width="14" height="18" rx="2" fill="none" stroke="#fff" stroke-width="2"/><path d="M4 6h8M4 10h8M4 14h5" stroke="#fff" stroke-width="1.6"/></svg></div>
    <div><h4>TAX WRITE OFF</h4><p>Sed ut perspiciatis unde omnis iste natus error sit volup-<br>tatem accusantium doloremque</p></div>
  </div>

  <h2 class="abs split-title" style="left:670px;top:1507px">DONATE YOUR CAR TODAY!</h2>
  <p class="abs split-text" style="left:670px;top:1546px;width:450px">Sed ut perspiciatis unde omnis iste natus error sit voluptatem accusantium dolore mque laudantium, totam rem aperiam, eaque ipsa quae ab illo inventore veritatis et quasi architecto beatae vitae dicta sunt explicabo.</p>
  <ul class="abs checks">
    <li><svg width="12" height="12" viewBox="0 0 12 12"><circle cx="6" cy="6" r="5" fill="none" stroke="#fff" stroke-width="1.4"/><path d="M3.5 6l2 2 3-3.5" stroke="#fff" stroke-width="1.4" fill="none"/></svg>You have no costs.</li>
    <li><svg width="12" height="12" viewBox="0 0 12 12"><circle cx="6" cy="6" r="5" fill="none" stroke="#fff" stroke-width="1.4"/><path d="M3.5 6l2 2 3-3.5" stroke="#fff" stroke-width="1.4" fill="none"/></svg>Free towing, running or not.</li>
    <li><svg width="12" height="12" viewBox="0 0 12 12"><circle cx="6" cy="6" r="5" fill="none" stroke="#fff" stroke-width="1.4"/><path d="M3.5 6l2 2 3-3.5" stroke="#fff" stroke-width="1.4" fill="none"/></svg>We issue you an IRS tax receipt.</li>
    <li><svg width="12" height="12" viewBox="0 0 12 12"><circle cx="6" cy="6" r="5" fill="none" stroke="#fff" stroke-width="1.4"/><path d="M3.5 6l2 2 3-3.5" stroke="#fff" stroke-width="1.4" fill="none"/></svg>We take care of all paperwork.</li>
    <li><svg width="12" height="12" viewBox="0 0 12 12"><circle cx="6" cy="6" r="5" fill="none" stroke="#fff" stroke-width="1.4"/><path d="M3.5 6l2 2 3-3.5" stroke="#fff" stroke-width="1.4" fill="none"/></svg>And we take care of DMV &amp; Smog issues.</li>
  </ul>
</section>

<footer>
  <div class="abs foot-col" style="left:100px">
    <h5>SAFE &amp; SECURE</h5>
    <div style="display:flex;gap:20px;margin-top:30px;align-items:center"><div class="badge-box"></div><div class="badge-seal"></div></div>
  </div>
  <div class="abs foot-col" style="left:378px">
    <h5>CONTACT US</h5>
    <ul class="contact-list">
      <li><svg width="14" height="14" viewBox="0 0 24 24"><path fill="#888" d="M6.6 10.8a15 15 0 0 0 6.6 6.6l2.2-2.2c.3-.3.7-.4 1-.2 1.1.4 2.3.6 3.6.6.6 0 1 .4 1 1V20c0 .6-.4 1-1 1A17 17 0 0 1 3 4c0-.6.4-1 1-1h3.5c.6 0 1 .4 1 1 0 1.3.2 2.5.6 3.6.1.3 0 .7-.2 1z"/></svg>1-800-555-0142 (Phone)</li>
      <li><svg width="14" height="14" viewBox="0 0 14 14"><rect x="3" y="1" width="8" height="4" fill="#888"/><rect x="1" y="5" width="12" height="6" fill="#888"/><rect x="3" y="9" width="8" height="4" fill="#bbb"/></svg>1-800-555-0142 (Fax)</li>
      <li><svg width="14" height="14" viewBox="0 0 14 14"><rect x="1" y="3" width="12" height="9" fill="#888"/><path d="M1 3l6 5 6-5" stroke="#fff" fill="none"/></svg><a>info@wheelsforheroes.org</a></li>
      <li><svg width="14" height="14" viewBox="0 0 14 14"><path d="M7 1a4 4 0 0 1 4 4c0 3-4 8-4 8S3 8 3 5a4 4 0 0 1 4-4z" fill="#888"/><circle cx="7" cy="5" r="1.5" fill="#fff"/></svg><span>WFH 1200 lorem ipsum Dummy<br>Text Lorem Ipsum</span></li>
    </ul>
  </div>
  <div class="abs foot-col" style="left:653px">
    <h5>NEWSLETTER</h5>
    <p>Register Your email address to get<br>information about us</p>
    <div class="email-box">Email Address</div>
    <span class="btn-sub">SUBSCRIBE</span>
  </div>
  <div class="abs foot-col" style="left:908px">
    <h5>FOLLOW US</h5>
    <p style="font-size:10.5px;line-height:19px;width:200px">Lorem ipsum dolor sit amet, conse ctetur adipiscing elit. Nulla in purus nibh. Donec ornare</p>
    <div class="social"><span></span><span></span><span></span><span></span><span></span></div>
  </div>
  <div class="abs copyright">© Copyright 2016 Wheels For Heroes.All Rights Reserved</div>
</footer>

</body>
</html>
```